New Business Card Design Project

We want a modern business card that catches the attention of other remodeling companies as well as homeowners. We would like it to be informative but still simple.

Target Market(s)

Residential and other Business's

Contact Information for Business Card

TrellBrix
Phone number is 6083927048
Address is
4817 SW 3rd Lane
Marrowfield, Ohio 43219
email is trellbrixco@quamlet.com

Requirements
Must have
• Our tagline
• Honest | Professional | Affordable

```html
<!DOCTYPE html>
<html lang="en">
<head>
<meta charset="utf-8">
<title>TrellBrix Business Card</title>
<link rel="stylesheet" href="https://fonts.googleapis.com/css2?family=Oswald:wght@600&family=Poppins:wght@400;500;700&display=swap">
<style>
  :root {
    --brand-blue: #2d62b0;
    --brand-orange: #d24a22;
    --brand-red: #e82a2e;
    --white: #ffffff;
    --stage: #e7e3dc;
  }
  * { box-sizing: border-box; margin: 0; padding: 0; }
  html, body {
    width: 900px; height: 1200px; overflow: hidden;
    background: var(--stage);
  }
  .canvas { position: relative; width: 900px; height: 1200px; }
  .card {
    position: absolute; left: 82px; width: 733px; height: 428px;
    border-radius: 26px; overflow: hidden;
    box-shadow: 0 8px 18px rgba(0,0,0,.25);
    font-family: "Poppins", sans-serif;
  }
  .card-front { top: 138px; background: var(--white); }
  .card-back {
    top: 634px;
    background: linear-gradient(90deg, #3f66b2 0%, #8a5686 48%, var(--brand-red) 100%);
  }
  .card-art { position: absolute; inset: 0; width: 100%; height: 100%; }
  .brand { position: absolute; left: 0; right: 0; text-align: center; }
  .brand-name {
    font-family: "Poppins", sans-serif; font-weight: 700;
    font-size: 70px; line-height: 1; letter-spacing: 2px;
  }
  .tagline {
    font-family: "Oswald", sans-serif; font-weight: 600;
    font-size: 20px; letter-spacing: .6px; margin-top: 6px;
  }
  .card-front .brand { top: 44px; }
  .card-front .brand-name, .card-front .tagline { color: var(--brand-blue); }
  .tagline .divider { color: var(--brand-orange); padding: 0 5px; }
  .card-back .brand { top: 166px; }
  .card-back .brand-name, .card-back .tagline, .card-back .tagline .divider { color: var(--white); }

  .holder { position: absolute; left: 48px; top: 272px; color: var(--white); }
  .holder-name { font-size: 22px; font-weight: 500; line-height: 1.3; }
  .holder-role { font-size: 16px; font-weight: 400; }
  .contact-list { position: absolute; color: var(--white); font-size: 16px; list-style: none; }
  .contact-left { left: 48px; top: 335px; }
  .contact-list li { display: flex; align-items: center; height: 25px; }
  .contact-left li svg { margin-right: 10px; }
  .contact-right { right: 38px; top: 335px; text-align: right; }
  .contact-right li { justify-content: flex-end; }
  .contact-right li svg { margin-left: 8px; }
  .contact-right .street { padding-right: 28px; }
</style>
</head>
<body>
<main class="canvas">
  <section class="card card-front" aria-label="Business card front">
    <svg class="card-art" viewBox="0 0 733 428" preserveAspectRatio="none" aria-hidden="true">
      <defs>
        <linearGradient id="frontGrad" x1="0" y1="0" x2="1" y2="0">
          <stop offset="0" stop-color="#5268b2"/>
          <stop offset=".45" stop-color="#9a5a80"/>
          <stop offset="1" stop-color="#e8282e"/>
        </linearGradient>
      </defs>
      <path d="M0,265 C180,225 330,305 470,298 C590,292 680,225 733,165 L733,428 L0,428 Z" fill="url(#frontGrad)"/>
      <path d="M0,330 C200,300 380,360 520,345 C620,335 690,300 733,290 L733,428 L0,428 Z" fill="#ffffff" opacity=".06"/>
      <path d="M0,226 C180,188 330,288 470,282 C590,277 680,205 733,142" fill="none" stroke="var(--brand-blue)" stroke-width="20"/>
      <path d="M0,188 C180,150 330,256 470,252 C585,248 680,180 733,118" fill="none" stroke="var(--brand-orange)" stroke-width="9"/>
    </svg>
    <div class="brand">
      <div class="brand-name">TRELLBRIX</div>
      <div class="tagline">HONEST<span class="divider">|</span>PROFESSIONAL<span class="divider">|</span>AFFORDABLE</div>
    </div>
    <div class="holder">
      <div class="holder-name">Dale Ferris</div>
      <div class="holder-role">Plumber Technician</div>
    </div>
    <ul class="contact-list contact-left">
      <li>
        <svg width="20" height="20" viewBox="0 0 20 20" aria-hidden="true"><circle cx="10" cy="10" r="8.5" fill="none" stroke="#fff" stroke-width="1.4"/><path d="M7 5.5l1.6 2-1 1.2c.6 1.3 1.5 2.2 2.7 2.8l1.2-1 2 1.6-.9 1.6c-3 0-6.4-3.4-6.4-6.4z" fill="#fff"/></svg>
        608 392 7048
      </li>
      <li>
        <svg width="20" height="20" viewBox="0 0 20 20" aria-hidden="true"><circle cx="10" cy="10" r="9" fill="#fff"/><rect x="5.5" y="7" width="9" height="6.5" rx="1" fill="none" stroke="#8a5a8c" stroke-width="1.2"/><path d="M5.8 7.4l4.2 3.2 4.2-3.2" fill="none" stroke="#8a5a8c" stroke-width="1.2"/></svg>
        trellbrixco@quamlet.com
      </li>
    </ul>
    <ul class="contact-list contact-right">
      <li>
        Marrowfield, Ohio 43219
        <svg width="20" height="20" viewBox="0 0 20 20" aria-hidden="true"><circle cx="10" cy="10" r="8.5" fill="none" stroke="#fff" stroke-width="1.4"/><path d="M10 4.5a3.3 3.3 0 0 0-3.3 3.3c0 2.5 3.3 6.5 3.3 6.5s3.3-4 3.3-6.5A3.3 3.3 0 0 0 10 4.5z" fill="none" stroke="#fff" stroke-width="1.3"/><circle cx="10" cy="7.9" r="1.1" fill="#fff"/></svg>
      </li>
      <li class="street">4817 SW 3rd Lane</li>
    </ul>
  </section>

  <section class="card card-back" aria-label="Business card back">
    <svg class="card-art" viewBox="0 0 733 428" preserveAspectRatio="none" aria-hidden="true">
      <path d="M0,110 C160,40 360,70 520,110 C620,135 690,120 733,100 L733,0 L0,0 Z" fill="#ffffff" opacity=".05"/>
      <path d="M0,345 C200,330 420,350 560,330 C640,318 700,300 733,290 L733,428 L0,428 Z" fill="#ffffff" opacity=".06"/>
      <path d="M420,200 C520,170 640,160 733,170 L733,428 L560,428 C640,360 560,250 420,200 Z" fill="#ffffff" opacity=".05"/>
    </svg>
    <div class="brand">
      <div class="brand-name">TRELLBRIX</div>
      <div class="tagline">HONEST<span class="divider">|</span>PROFESSIONAL<span class="divider">|</span>AFFORDABLE</div>
    </div>
  </section>
</main>
</body>
</html>
```